Email Signature

Our company is having its 10th anniversary in 2021. We would like a new email signature to celebrate the occasion. Attached is our business card design.
Please refer to our website for actual contact details.
www.corvanhold.com.au

Industry/Entity Type

Real Estate

Requirements
Must have
• Our logo
Email
Contact Numbers
Address
Website address

Celebrating 10 years in 2021
Nice to have
• Something that blends the designs of our website and business card

```html
<!DOCTYPE html>
<html lang="en">
<head>
<meta charset="utf-8">
<title>Email Signature</title>
<link href="https://fonts.googleapis.com/css2?family=Open+Sans:wght@400;600;700&family=Dancing+Script:wght@500&display=swap" rel="stylesheet">
<style>
  :root {
    --page-bg: #eceef0;
    --card-bg: #ffffff;
    --brand-blue: #1d5fa8;
    --icon-blue: #3aa6e0;
    --text-dark: #3d3d3d;
    --text-mid: #555555;
    --skyline-tint: #dcebf6;
  }
  * { margin: 0; padding: 0; box-sizing: border-box; }
  html, body { width: 1200px; height: 840px; overflow: hidden; }
  body {
    background: var(--page-bg);
    font-family: "Open Sans", Arial, sans-serif;
    position: relative;
  }
  .signature {
    position: absolute;
    left: 153px; top: 338px;
    width: 939px; height: 235px;
    background: var(--card-bg);
    box-shadow: 0 6px 14px rgba(0,0,0,0.22);
    overflow: hidden;
  }
  .skyline-band {
    position: absolute;
    left: 0; right: 0; bottom: 0; height: 62px;
    background: linear-gradient(to bottom, rgba(220,235,246,0) 0%, var(--skyline-tint) 100%);
  }
  .brand-name {
    position: absolute;
    left: 0; width: 400px; top: 100px;
    text-align: center;
    font-size: 25px; font-weight: 600;
    color: var(--brand-blue);
    letter-spacing: 0.5px;
  }
  .brand-mark {
    display: inline-block;
    width: 14px; height: 14px;
    background: var(--brand-blue);
    margin-right: 10px;
    vertical-align: 2px;
  }
  .services {
    position: absolute;
    left: 22px; top: 155px;
    font-size: 11.5px; color: #222;
    letter-spacing: 0.2px;
    white-space: nowrap;
  }
  .anniversary {
    position: absolute;
    left: 55px; top: 183px;
    font-family: "Dancing Script", cursive;
    font-size: 30px; color: #333;
  }
  .person-name {
    position: absolute;
    left: 413px; top: 8px;
    font-size: 30px; font-weight: 700;
    color: var(--brand-blue);
  }
  .person-role {
    position: absolute;
    left: 413px; top: 50px;
    font-size: 20px; color: var(--text-mid);
  }
  .contact {
    position: absolute;
    display: flex; align-items: center;
    font-size: 20px; font-weight: 700;
    color: var(--text-dark);
    white-space: nowrap;
  }
  .contact svg { width: 18px; height: 18px; flex: none; margin-right: 16px; }
  .contact svg * { fill: var(--icon-blue); }
  .address-lines { line-height: 26px; }
  .address-lines span { display: block; }
  .address-lines span + span { margin-left: -16px; }
</style>
</head>
<body>
  <section class="signature">
    <div class="skyline-band" role="img" aria-label="Faint city skyline silhouette along the bottom edge"></div>

    <div class="brand-name"><span class="brand-mark"></span>CORVAN GROUP</div>
    <div class="services">BUILDING MANAGEMENT · CONCIERGE · CARETAKING · CLEANING</div>
    <div class="anniversary">Celebrating 10 years in 2021</div>

    <div class="person-name">Daniel R, Harwell</div>
    <div class="person-role">Owner</div>

    <div class="contact" style="left:413px; top:99px;">
      <svg viewBox="0 0 18 18"><path d="M5 1h8a1 1 0 0 1 1 1v14a1 1 0 0 1-1 1H5a1 1 0 0 1-1-1V2a1 1 0 0 1 1-1zm1 2v10h6V3z"/></svg>
      561-555-0142
    </div>
    <div class="contact" style="left:413px; top:126px;">
      <svg viewBox="0 0 18 18"><path d="M2 7c0-3 3-4 7-4s7 1 7 4v1h-4V6H6v2H2zM4 9h10l2 6H2z"/></svg>
      561-555-0187
    </div>
    <div class="contact" style="left:643px; top:99px;">
      <svg viewBox="0 0 18 18"><path d="M1 4h16v10H1zM2 5l7 5 7-5v1l-7 5-7-5z"/></svg>
      danharwell@mailbox.com
    </div>
    <div class="contact" style="left:643px; top:126px;">
      <svg viewBox="0 0 18 18"><path d="M9 1a8 8 0 1 1 0 16A8 8 0 0 1 9 1zm0 2a6 6 0 1 0 0 12A6 6 0 0 0 9 3zm-1 2h2v8H8z"/></svg>
      www.corvanhold.com.au
    </div>
    <div class="contact" style="left:413px; top:157px; align-items:flex-start;">
      <svg viewBox="0 0 18 18" style="margin-top:4px;"><path d="M9 1a6 6 0 0 1 6 6c0 4-6 10-6 10S3 11 3 7a6 6 0 0 1 6-6zm0 3.5a2.5 2.5 0 1 0 0 5 2.5 2.5 0 0 0 0-5z"/></svg>
      <div class="address-lines">
        <span>2240 s. Harbor Avenue #210</span>
        <span>Bayview Shores, Florida 33400</span>
      </div>
    </div>
  </section>
</body>
</html>
```